Harlow Ridge Growers and Nursery needs a business street sign.

I have three businesses located at the same address: The Harlow Ridge Growers & Nursery, The Bramble Nook, and The Quarry Commons. I am looking for a 4’ x 8’ street sign to represent all three businesses as one retail experience. It needs to be eye catching yet simple enough that people can fully read it while driving by. I have logos for the greenhouse and village however I do not have anything for The Bramble Nook. I’m looking for some type of font that’s similar or in between the two attached logos for The Bramble Nook.

• Horizontal Sign, Eye catching, yet simple design so people see it while driving by.
• Horizontal Sign
• I’m open to the design being both vertical and horizontal. Please provide both options

```html
<!DOCTYPE html>
<html lang="en">
<head>
<meta charset="utf-8">
<title>Harlow Ridge Growers, The Bramble Nook &amp; The Quarry Commons — Street Sign</title>
<link href="https://fonts.googleapis.com/css2?family=Antonio:wght@400&family=Montserrat:wght@600;800;900&family=Great+Vibes&display=swap" rel="stylesheet">
<style>
  :root {
    --green: #0b6b3a;
    --red: #8a2a22;
    --line: #c9705a;
    --ink: #161616;
    --paper: #ffffff;
    --backdrop: #e4e6e8;
  }
  * { margin: 0; padding: 0; box-sizing: border-box; }
  html, body { width: 1200px; height: 1200px; overflow: hidden; }
  body {
    background: var(--backdrop);
    display: flex; align-items: center; justify-content: center;
    font-family: "Montserrat", sans-serif;
  }
  .sign {
    position: relative;
    width: 742px; height: 1120px;
    background: var(--paper);
    overflow: hidden;
  }
  .sign__frame { position: absolute; inset: 0; width: 100%; height: 100%; }

  .brand-row {
    position: absolute; top: 62px; left: 60px; right: 40px;
    display: flex; justify-content: space-between; align-items: center;
  }
  .brand {
    font-family: "Montserrat", sans-serif;
    font-weight: 800;
    color: var(--green);
    font-size: 30px; line-height: 1.05;
    text-align: center;
  }
  .brand--nook { width: 290px; }
  .brand--harlow { width: 330px; font-size: 28px; }
  .brand--commons {
    position: absolute; top: 196px; left: 0; right: 0;
    color: var(--red); font-size: 56px; line-height: 1;
  }

  .gallery { position: absolute; top: 348px; left: 0; width: 742px; height: 170px; }

  .headline {
    position: absolute; top: 540px; left: 0; right: 0;
    text-align: center;
    font-family: "Antonio", sans-serif; font-weight: 400;
    font-size: 98px; line-height: 1; color: var(--ink);
    letter-spacing: 2px;
  }
  .subline {
    position: absolute; top: 656px; left: 0; right: 0;
    text-align: center; color: var(--green);
    font-weight: 600; font-size: 40px; line-height: 44px; letter-spacing: 1px;
  }
  .subline__first { display: block; padding-right: 40px; }
  .subline__second { position: relative; display: inline-block; padding-left: 70px; }
  .script-amp {
    font-family: "Great Vibes", cursive; color: var(--ink);
    font-weight: 400; letter-spacing: 0;
  }
  .subline .script-amp {
    position: absolute; left: 0; top: -22px; font-size: 84px; line-height: 1;
  }
  .shop-name {
    position: absolute; top: 806px; left: 0; right: 0;
    text-align: center; color: var(--green);
    font-weight: 800; font-size: 36px; line-height: 44px; letter-spacing: 1px;
  }
  .joiner {
    position: absolute; top: 852px; left: 0; right: 0;
    text-align: center; font-size: 50px; line-height: 50px;
  }
  .village-name {
    position: absolute; top: 906px; left: 0; right: 0;
    text-align: center; color: var(--green);
    font-weight: 900; font-size: 50px; line-height: 1.18; letter-spacing: 3px;
  }
</style>
</head>
<body>
  <main class="sign">
    <svg class="sign__frame" viewBox="0 0 742 1120" aria-hidden="true">
      <polygon points="6,6 92,6 6,78" fill="var(--green)"/>
      <polyline points="6,150 90,95 6,20" fill="none" stroke="var(--red)" stroke-width="2"/>
      <polyline points="92,6 270,6 295,-20" fill="none" stroke="var(--red)" stroke-width="2"/>
      <polygon points="736,1114 736,1032 690,1032 590,1114" fill="var(--green)"/>
      <polyline points="736,900 680,980 736,1040" fill="none" stroke="var(--line)" stroke-width="2"/>
      <polyline points="414,1118 460,1032 690,1032" fill="none" stroke="var(--line)" stroke-width="2"/>
    </svg>

    <header class="brand-row">
      <div class="brand brand--nook">The Bramble<br>Nook</div>
      <div class="brand brand--harlow">Harlow Ridge<br>Growers &amp; Nursery</div>
    </header>
    <div class="brand brand--commons">Quarry<br>Commons</div>

    <svg class="gallery" viewBox="0 0 742 170">
      <defs>
        <linearGradient id="field" x1="0" y1="0" x2="0" y2="1">
          <stop offset="0" stop-color="#c9d3c8"/><stop offset="0.45" stop-color="#4f7f3a"/><stop offset="1" stop-color="#d7b32a"/>
        </linearGradient>
        <linearGradient id="tunnel" x1="0" y1="0" x2="0" y2="1">
          <stop offset="0" stop-color="#eef1ee"/><stop offset="0.5" stop-color="#9fb39a"/><stop offset="1" stop-color="#2f5a2a"/>
        </linearGradient>
        <linearGradient id="blooms" x1="0" y1="0" x2="1" y2="1">
          <stop offset="0" stop-color="#d94a7c"/><stop offset="0.55" stop-color="#b85aa8"/><stop offset="1" stop-color="#f0b623"/>
        </linearGradient>
      </defs>
      <polygon role="img" aria-label="Rows of potted mums in a greenhouse" points="44,85 84,3 226,3 266,85 226,167 84,167" fill="url(#field)" stroke="var(--red)" stroke-width="3"/>
      <polygon role="img" aria-label="Plastic hoop greenhouse filled with seedlings" points="258,85 298,3 440,3 480,85 440,167 298,167" fill="url(#tunnel)" stroke="var(--paper)" stroke-width="3"/>
      <polygon role="img" aria-label="Colourful flower baskets and sunflowers on display" points="472,85 512,3 654,3 694,85 654,167 512,167" fill="url(#blooms)" stroke="var(--red)" stroke-width="3"/>
    </svg>

    <h1 class="headline">THE HARLOW RIDGE</h1>
    <p class="subline">
      <span class="subline__first">GROWERS</span>
      <span class="subline__second"><span class="script-amp">&amp;</span>NURSERY</span>
    </p>
    <p class="shop-name">THE BRAMBLE NOOK</p>
    <p class="joiner script-amp">&amp;</p>
    <p class="village-name">THE QUARRY<br>COMMONS</p>
  </main>
</body>
</html>
```